Create a Magazine Ad for an asbestos law firm

we need an 8 X 13 ad to be on the back of a magazine cover. We have the text Attached and want a similar look and feel to our website : www.claimsharbor-help.com. The ad should be targeted to white males 55 years or older who are conservative and worked in industry or industrial plants. The main offer is a free case review and trying to get them to call the telephone number.

Target Market(s)

White collar men who worked in industrial plants. Age 55 years or older.

Industry/Entity Type

Legal

Requirements
Must have
• Pictures of white middle class conservative man or man and woman
Nice to have
• look at www.claimsharbor-help.com to an. idea of what we are looking for

```html
<!DOCTYPE html>
<html lang="en">
<head>
<meta charset="utf-8">
<title>ClaimsHarbor.com Magazine Ad</title>
<link rel="stylesheet" href="https://fonts.googleapis.com/css2?family=Merriweather:wght@400;700;900&family=Montserrat:wght@400;600;700&display=swap">
<style>
:root{
  --backdrop:#8a8a8a;
  --navy:#23415e;
  --band-blue:#34709a;
  --band-blue-dark:#2c5f85;
  --heading-blue:#2d6590;
  --panel-blue:#e0f1f9;
  --red:#c8423a;
  --red-dark:#8f1d1b;
  --ink:#2b2b2b;
  --white:#ffffff;
}
*{margin:0;padding:0;box-sizing:border-box}
html,body{width:1200px;height:1200px;overflow:hidden;background:var(--backdrop)}
.ad{position:absolute;left:283px;top:81px;width:640px;height:1041px;background:var(--white);overflow:hidden;font-family:'Montserrat',sans-serif;color:var(--ink)}
.photo{position:absolute;top:0;height:257px}
.photo-debris{left:0;width:213px;background:linear-gradient(160deg,#8a7a68 0%,#9d9a92 45%,#6f6d68 75%,#c9a23a 86%,#c84a2e 100%)}
.photo-doctor{left:211px;width:227px;background:linear-gradient(135deg,#1f4f78,#3e7fae 60%,#9fd3e6);border-radius:0 0 24px 24px;border:2px solid var(--white);border-top:none}
.photo-sign{left:438px;width:202px;background:linear-gradient(150deg,#7d7d7d 0%,#a5a5a5 40%,#e2d526 60%,#d8c81f 80%,#5e5e5e 100%)}
.name-tab{position:absolute;left:154px;top:0;width:334px;height:63px}
.name-tab svg{position:absolute;inset:0}
.brand-name{position:absolute;left:0;right:0;top:13px;text-align:center;font-family:'Montserrat',sans-serif;font-weight:700;font-size:21px;color:var(--navy)}
.brand-line{position:absolute;left:0;right:0;top:41px;text-align:center;font-weight:600;font-size:7px;letter-spacing:1.4px;color:var(--navy)}
.headline-band{position:absolute;left:0;top:260px;width:640px;height:111px;background:linear-gradient(90deg,var(--band-blue-dark),var(--band-blue) 50%,var(--band-blue-dark));display:flex;align-items:center;justify-content:center}
.headline{font-family:'Merriweather',serif;font-weight:900;font-size:31px;line-height:38px;color:var(--white);text-align:center}
.cta-band{position:absolute;left:0;top:855px;width:640px;height:186px;background:var(--red)}
.settlements{position:absolute;left:34px;top:371px;width:285px;height:724px;max-height:723px;background:var(--panel-blue);border-radius:0 0 0 50px;padding:22px 14px 0 29px;box-shadow:0 8px 10px -6px rgba(90,10,10,.5)}
.settlements h2{font-weight:700;font-size:20.5px;line-height:24.5px;color:var(--heading-blue)}
.settlements .intro{font-size:12.3px;line-height:14.7px;margin-top:3px;color:#2a2a2a}
.award{margin-top:17px}
.award.first{margin-top:27px}
.award-amount{font-weight:700;font-size:20px;line-height:21px;color:var(--heading-blue)}
.award-source{font-size:12.5px;line-height:15px;color:#333}
.info{position:absolute;left:344px;top:397px;width:270px}
.info .lead{font-weight:600;font-size:10.4px;line-height:13.3px;color:#222}
.info ul{list-style:none;margin:7px 0 10px}
.info li{position:relative;padding-left:12px;font-size:9.6px;line-height:14.5px;color:#444}
.info li::before{content:"";position:absolute;left:2px;top:5px;width:4.5px;height:4.5px;border-radius:50%;background:var(--red)}
.trust-box{position:absolute;left:342px;top:618px;width:281px;height:219px;border-radius:12px;background:linear-gradient(135deg,#d9eef8,#eaf6fb 60%,#dff0f8);padding:16px 12px 0 21px}
.trust-figure{font-weight:700;font-size:25px;line-height:27px;color:var(--red)}
.trust-title{font-weight:700;font-size:19.3px;line-height:25px;color:var(--heading-blue)}
.trust-body{font-size:9.6px;line-height:12.4px;color:#333;margin-top:6px}
.cta{position:absolute;left:349px;top:873px;width:285px;color:var(--white);font-family:'Merriweather',serif}
.cta-text{font-size:12.2px;line-height:15.6px}
.cta-text b{font-weight:900}
.cta-push{font-weight:700;font-size:17px;margin-top:8px;margin-left:-2px}
.phone{position:absolute;left:342px;top:961px;width:268px;height:39px;border-radius:20px;background:var(--red-dark);display:flex;align-items:center;padding-left:6px}
.phone-icon{width:29px;height:29px;border-radius:50%;background:var(--white);display:flex;align-items:center;justify-content:center}
.phone-number{margin-left:7px;font-weight:700;font-size:20.5px;color:var(--white);word-spacing:4px}
.firm{position:absolute;left:348px;top:1007px;font-family:'Merriweather',serif;font-size:9.6px;color:var(--white);display:flex;align-items:center;gap:5px}
</style>
</head>
<body>
<div class="ad">
  <div class="photo photo-debris" role="img" aria-label="Pile of broken asbestos roofing sheets behind blurred stop tape"></div>
  <div class="photo photo-sign" role="img" aria-label="Yellow Danger Asbestos warning sign on a grey wall"></div>
  <div class="photo photo-doctor" role="img" aria-label="Medical worker holding a small chalkboard reading Mesothelioma"></div>

  <div class="name-tab">
    <svg width="334" height="63" viewBox="0 0 334 63"><polygon points="0,0 334,0 314,63 35,63" fill="#ffffff"/></svg>
    <div class="brand-name">ClaimsHarbor.com</div>
    <div class="brand-line">FREE CASE REVIEWS FOR ASBESTOS VICTIMS</div>
  </div>

  <div class="headline-band">
    <h1 class="headline">Diagnosed with Mesothelioma,<br>You could be Owed Compensation</h1>
  </div>

  <div class="cta-band"></div>

  <section class="settlements">
    <h2>How much<br>Money Can People<br>Receive from a<br>Mesothelioma<br>Case?</h2>
    <p class="intro">Depending on where you were exposed and a few other factors, you can get a settlement from 6 to 7 figures. Here are a few examples of Mesothelioma Settlements received by our clients. These figures are the total compensation after all attorney fees and expenses are deducted.</p>
    <div class="award first"><div class="award-amount">$6,142,500</div><div class="award-source">Exposed through heavy duty vehicles</div></div>
    <div class="award"><div class="award-amount">$6,033,510</div><div class="award-source">Exposed through general contracting</div></div>
    <div class="award"><div class="award-amount">$5,939,010</div><div class="award-source">Exposed through boat repair</div></div>
    <div class="award"><div class="award-amount">$3,921,750</div><div class="award-source">Exposed through navy service</div></div>
    <div class="award"><div class="award-amount">$3,600,450</div><div class="award-source">Exposed through navy service</div></div>
    <div class="award"><div class="award-amount">$2.5 Million</div><div class="award-source">Exposed from Brand-Name Talcum<br>Baby Powder</div></div>
  </section>

  <section class="info">
    <p class="lead">It's very likely you developed this disease through asbestos exposure. Mesothelioma patients are getting multi-million dollar settlements, decades later, from:</p>
    <ul>
      <li>Exposure to asbestos products,</li>
      <li>Ex-employers, or</li>
      <li>Talcum baby powder companies.</li>
    </ul>
    <p class="lead">We can help you find out if you qualify<br>for a case in minutes.</p>
    <ul>
      <li>We'll analyze your situation at no cost</li>
      <li>Determine how much compensation you could be entitled too</li>
      <li>Show you the next steps to get what you're owed</li>
    </ul>
  </section>

  <section class="trust-box">
    <div class="trust-figure">$30 Billion</div>
    <div class="trust-title">is Available in Trust<br>for Mesothelioma<br>Patients</div>
    <p class="trust-body">Depending on where you were exposed and a few other factors, you can get a settlement from 6 to 7 figures. Here are a few examples of Mesothelioma Settlements received by our clients. These figures are the total compensation after all attorney fees and expenses are deducted.</p>
  </section>

  <section class="cta">
    <p class="cta-text">Find out if you're <b>Eligible</b>, for <b>FREE</b>, in <b>Minutes</b>. We'll evaluate your situation and tell you what your case could be worth.</p>
    <p class="cta-push">Get your Free evaluation now!</p>
  </section>

  <div class="phone">
    <div class="phone-icon">
      <svg width="18" height="18" viewBox="0 0 24 24"><path d="M6.6 10.8c1.4 2.8 3.8 5.1 6.6 6.6l2.2-2.2c.3-.3.7-.4 1-.2 1.1.4 2.3.6 3.6.6.6 0 1 .4 1 1V20c0 .6-.4 1-1 1C10.6 21 3 13.4 3 4c0-.6.4-1 1-1h3.5c.6 0 1 .4 1 1 0 1.3.2 2.5.6 3.6.1.3 0 .7-.2 1L6.6 10.8z" fill="#8f1d1b"/></svg>
    </div>
    <span class="phone-number">Call 1.800.555.0142</span>
  </div>

  <div class="firm">
    <svg width="8" height="11" viewBox="0 0 8 11"><path d="M4 0C1.8 0 0 1.8 0 4c0 3 4 7 4 7s4-4 4-7c0-2.2-1.8-4-4-4zm0 5.5A1.5 1.5 0 1 1 4 2.5a1.5 1.5 0 0 1 0 3z" fill="#ffffff"/></svg>
    <span>Whitfield &amp; Arden, LLP, Thomas Whitfield, Houston, TX</span>
  </div>
</div>
</body>
</html>
```